4 x Florist Footpath Signage Boards that are consistant with each other for a modern florist

Eye catching, easy to read. little bit floral.
See example attached for wording. We are a modern florist in a country town.
This will be out on the street and needs to stand out!!

The Signage Panels
1. Valentines Day - 14th Feb
2. Workshop Signage boards - see attached example
3. Mothers Day Signage Board - 'Treat mum this Mothers Day'
4. We Are Open

Attached is a copy of the design guidelines and the template. the base of the sign is white.

Target Market(s)

Modern

Industry/Entity Type

Florist

Font styles to use
Sans Serif

Colors
eea4c8
f59296
ffffff
757575

Requirements
Must have
• flowers
• weddings
• giftware
• workshops
• flowers make people happy
• odettemarshpetals.co.nz
Nice to have
• Logo
• little bit of floral or greenery
• my shop is modem and industrial
Should not have
• Needs to be able to read easy

```html
<!DOCTYPE html>
<html lang="en">
<head>
<meta charset="utf-8">
<title>Mothers Day Signage Board</title>
<link href="https://fonts.googleapis.com/css2?family=Great+Vibes&family=Montserrat:wght@400;700&display=swap" rel="stylesheet">
<style>
  :root {
    --backdrop: #ececec;
    --board: #fbeff0;
    --gold: #c9a233;
    --gold-deep: #b18a22;
    --ink: #111111;
    --pill: #f6d3d9;
    --rose-light: #f4c6cc;
    --rose: #e9a0aa;
    --leaf: #2f6f80;
    --leaf-light: #7fb5b9;
    --petal-yellow: #f3cf3b;
  }
  * { margin: 0; padding: 0; box-sizing: border-box; }
  html, body { width: 1200px; height: 774px; overflow: hidden; }
  body {
    background: var(--backdrop);
    font-family: "Montserrat", sans-serif;
  }
  .sign-board {
    position: absolute;
    left: 370px;
    top: 40px;
    width: 460px;
    height: 694px;
    background: var(--board);
    box-shadow: 0 6px 18px rgba(0,0,0,0.18);
    overflow: hidden;
  }
  .floral {
    position: absolute;
  }
  .floral--corner-rose {
    left: -10px; top: -14px; width: 168px; height: 222px;
    border-radius: 0 0 60% 40%;
    background: radial-gradient(circle at 45% 45%, var(--rose) 0%, var(--rose-light) 55%, rgba(244,198,204,0) 75%);
  }
  .floral--top-right {
    left: 171px; top: 14px; width: 227px; height: 242px;
    border-radius: 50%;
    background:
      radial-gradient(circle at 55% 40%, var(--rose) 0%, var(--rose-light) 28%, rgba(244,198,204,0) 42%),
      radial-gradient(ellipse at 60% 55%, rgba(127,181,185,0.55) 0%, rgba(47,111,128,0.25) 45%, rgba(47,111,128,0) 68%);
  }
  .floral--bottom-left {
    left: 26px; top: 428px; width: 264px; height: 252px;
    border-radius: 50%;
    background:
      radial-gradient(circle at 58% 65%, var(--rose) 0%, var(--rose-light) 24%, rgba(244,198,204,0) 38%),
      radial-gradient(ellipse at 45% 50%, rgba(127,181,185,0.55) 0%, rgba(47,111,128,0.25) 45%, rgba(47,111,128,0) 68%);
  }
  .frame {
    position: absolute;
    left: 0; top: 0;
    width: 460px; height: 694px;
  }
  .brand-name {
    position: absolute;
    left: 180px; top: 198px;
    width: 110px;
    text-align: center;
    font-family: "Montserrat", sans-serif;
    font-weight: 400;
    font-size: 9px;
    letter-spacing: 2.5px;
    line-height: 13px;
    color: var(--gold);
    text-transform: uppercase;
  }
  .headline {
    position: absolute;
    left: 0; top: 302px;
    width: 460px;
    text-align: center;
    font-family: "Great Vibes", cursive;
    font-size: 34px;
    color: var(--gold);
  }
  .divider {
    position: absolute;
    left: 146px; top: 359px;
    width: 172px; height: 1px;
    background: var(--gold);
  }
  .divider::after {
    content: "";
    position: absolute;
    left: 83px; top: -2px;
    width: 5px; height: 5px;
    border-radius: 50%;
    background: var(--gold);
  }
  .tagline {
    position: absolute;
    left: 0; top: 374px;
    width: 460px;
    text-align: center;
    font-family: "Great Vibes", cursive;
    font-size: 24px;
    color: var(--gold);
  }
  .shop-online {
    position: absolute;
    left: 278px; top: 620px;
    width: 160px;
    text-align: center;
    font-weight: 700;
    font-size: 20px;
    color: var(--ink);
  }
  .web-address {
    position: absolute;
    left: 272px; top: 649px;
    width: 170px; height: 20px;
    border-radius: 4px;
    background: var(--pill);
    text-align: center;
    line-height: 20px;
    font-weight: 700;
    font-size: 9.5px;
    color: var(--ink);
    text-transform: uppercase;
  }
</style>
</head>
<body>
  <main class="sign-board">
    <div class="floral floral--corner-rose" role="img" aria-label="Large illustrated pink peony in the top-left corner"></div>
    <div class="floral floral--top-right" role="img" aria-label="Illustrated bouquet of pink peony, coral and yellow blossoms with teal leaves"></div>

    <svg class="frame" viewBox="0 0 460 694" aria-hidden="true">
      <polygon points="230,104 444,344 230,584 16,344" fill="none" stroke="var(--gold)" stroke-width="2"/>
      <polygon points="230,130 420,344 230,558 40,344" fill="none" stroke="var(--gold-deep)" stroke-width="1.5"/>
    </svg>

    <div class="floral floral--bottom-left" role="img" aria-label="Illustrated bouquet of pink peony, coral and yellow blossoms with teal leaves"></div>

    <p class="brand-name">Odette<br>Marsh<br>Petals</p>
    <h1 class="headline">Mothers Day SignageBoard</h1>
    <div class="divider"></div>
    <p class="tagline">Treat mum this Mothers Day</p>

    <p class="shop-online">SHOP ONLINE</p>
    <p class="web-address">odettemarshpetals.co.nz</p>
  </main>
</body>
</html>
```